Penwick Insurance Post Card

Specializing in “Towing & Transportation Insurance”
See our website at http://penwickins-example.net/ for ideas on colors fonts etc.

Target Market(s)

Towing Companies

Font styles to use
Serif
Sans Serif

Requirements
Must have
• Specializing in “Towing & Transportation Insurance”
• Welcome to Penwick Insurance:
• 2nd sentence (With our Agency, we work to make ourselves available to your business for when you need us most to keep your business moving forward.)
• 3rd Sentence: (Our customers were in mind when developing our agency and will continue to find new ways to make doing business with us easier.)
• We Offer: Change “Dealers Physical Damage” to “Auto Dealer Liability” & “Garage Liability” to “Garage Repair Liability”
• Our address: 418 5th St NW, Suite B Decatur, AL 35602
• Email Address: PenwickInfo@velmorlink.example

```html
<!DOCTYPE html>
<html lang="en">
<head>
<meta charset="utf-8">
<title>Penwick Insurance Post Card</title>
<link href="https://fonts.googleapis.com/css2?family=Questrial&family=Oswald:wght@500&display=swap" rel="stylesheet">
<style>
:root{
  --bg:#e9e9e9;
  --white:#ffffff;
  --navy:#10406f;
  --blue:#1d6aa6;
  --blue-light:#2e86c1;
  --gold:#f4b93f;
  --gold-light:#ffd978;
  --ink:#1f3550;
  --line:#8c8c8c;
  --photo-a:#9aa3a2;
  --photo-b:#6c7478;
}
*{box-sizing:border-box;margin:0;padding:0}
html,body{width:689px;height:1200px;overflow:hidden}
body{background:var(--bg);font-family:"Questrial",sans-serif;color:var(--ink);position:relative}
.card{position:absolute;left:24px;width:641px;height:456px;background:var(--white);box-shadow:0 2px 10px rgba(0,0,0,.18);overflow:hidden}
.front{top:110px}
.back{top:634px}
.photo{position:absolute;background:linear-gradient(160deg,var(--photo-a),var(--photo-b))}
.photo-top{left:9px;top:9px;width:440px;height:216px;background:linear-gradient(165deg,#b9c2c0,#8c9490 55%,#5e6a5a)}
.photo-bottom{left:9px;top:231px;width:440px;height:216px;background:linear-gradient(170deg,#a39a90,#5a6a86 55%,#2e3336)}
.brand{position:absolute;text-align:center}
.brand-name{font-family:"Questrial",sans-serif;color:var(--navy);text-transform:uppercase;letter-spacing:2px;line-height:1.1}
.brand-name span{display:block;font-size:.42em;letter-spacing:.9em}
.brand-tag{font-style:italic;color:#b07d14;font-size:8px;margin-top:4px;border-top:1px solid var(--navy);padding-top:3px}
.front .brand{left:385px;top:12px;width:250px;background:var(--white);height:112px;padding-top:12px}
.front .brand-name{font-size:38px}
.panel{position:absolute;background:linear-gradient(180deg,var(--navy),var(--blue) 55%,var(--blue-light));color:var(--white)}
.front .panel{left:290px;top:117px;width:342px;height:298px;clip-path:polygon(100px 0,100% 0,100% 100%,0 100%)}
.welcome{margin-left:96px;margin-top:10px;border-top:1px solid rgba(255,255,255,.6);border-bottom:1px solid rgba(255,255,255,.6);padding:5px 0;text-align:center;font-size:13px;text-transform:uppercase}
.welcome b{font-weight:400;letter-spacing:.3px;font-family:"Questrial",sans-serif;text-shadow:0 0 .5px #fff}
.intro{margin:10px 6px 0 88px;font-size:11px;line-height:1.3;text-align:center}
.intro p+p{margin-top:12px}
.tag{display:inline-block;background:linear-gradient(180deg,var(--gold-light),var(--gold));color:var(--navy);text-transform:uppercase;clip-path:polygon(8px 0,100% 0,calc(100% - 8px) 100%,0 100%)}
.offer-tag{position:absolute;left:148px;top:150px;font-size:15px;padding:3px 22px}
.offer{position:absolute;left:40px;top:183px;display:flex;gap:30px;font-size:11px;list-style:none}
.offer ul{list-style:none}
.offer li{line-height:16px;padding-left:13px;position:relative}
.offer li::before{content:"";position:absolute;left:0;top:4px;width:8px;height:8px;border-radius:50%;border:1.5px solid #cfe3f3}
.footer{position:absolute;background:var(--white);display:flex;align-items:center;color:var(--ink);font-size:11px}
.front .footer{left:290px;top:415px;width:342px;height:32px;padding-left:8px}
.contact{display:flex;flex-direction:column;gap:3px}
.contact div{display:flex;align-items:center;gap:5px}
.icon{width:11px;height:11px;border-radius:50%;background:var(--navy);display:inline-block}
.phone{display:flex;align-items:center;gap:5px;margin-left:auto;padding:0 8px 0 10px;border-left:1px solid var(--line);font-family:"Oswald",sans-serif;font-size:19px;color:var(--navy)}
.phone svg{width:14px;height:14px}
/* back */
.back .brand{left:50px;top:12px;width:180px}
.back .brand-name{font-size:28px}
.back .panel{left:9px;top:85px;width:355px;height:335px;clip-path:polygon(0 0,100% 0,96% 100%,0 100%);padding:12px 20px 0 9px}
.about-tag{display:block;width:118px;margin:0 auto;text-align:center;font-size:13px;padding:2px 0}
.about{margin-top:10px;font-size:9.6px;line-height:1.28;text-align:justify}
.states-tag{display:block;width:240px;margin:14px auto 0;text-align:center;font-size:10px;padding:3px 0}
.map{position:relative;width:220px;height:110px;margin:8px auto 0;background:linear-gradient(180deg,#e9eef3,#c7d3de);border-radius:20px 40px 30px 50px}
.state{position:absolute;font-size:8px;background:var(--gold);color:var(--navy);padding:1px 5px;border-radius:2px}
.back .footer{left:9px;top:420px;width:352px;height:27px;padding-left:6px;font-size:9.5px}
.back .phone{font-size:16px}
.address{position:absolute;left:378px;top:18px;font-size:11px;line-height:1.3;color:#555}
.stamp{position:absolute;left:546px;top:22px;width:74px;height:66px;border:1px solid #777}
.rule{position:absolute;left:383px;width:237px;border-top:1px solid #777}
</style>
</head>
<body>

<section class="card front">
  <div class="photo photo-top" role="img" aria-label="Photo of a silver car beside a tilted flatbed tow truck with a mechanic at work"></div>
  <div class="photo photo-bottom" role="img" aria-label="Photo of a damaged blue car loaded on a flatbed tow truck"></div>
  <div class="brand">
    <div class="brand-name">Penwick<span>Insurance</span></div>
    <div class="brand-tag">Specializing in Towing &amp; Transportation Insurance</div>
  </div>
  <div class="panel">
    <div class="welcome">Welcome to <b>Penwick Insurance</b></div>
    <div class="intro">
      <p>With our Agency, we work to make ourselves available to your business for when you need us most to keep your business moving forward.</p>
      <p>Our customers were in mind when developing our agency and will continue to find new ways to make doing business with us easier.</p>
    </div>
    <span class="tag offer-tag">We Offer</span>
    <div class="offer">
      <ul><li>Auto Liability</li><li>General Liability</li><li>Garage Repair Liability</li><li>Garagekeepers</li><li>Auto Dealer Liability</li><li>OnHook</li></ul>
      <ul><li>Cargo</li><li>Property</li><li>Wrongful Repossession</li><li>Umbrella/Excess</li><li>Workers Compensation</li></ul>
    </div>
  </div>
  <div class="footer">
    <div class="contact">
      <div><i class="icon"></i>penwickins-example.net</div>
      <div><i class="icon"></i>PenwickInfo@velmorlink.example</div>
    </div>
    <div class="phone"><svg viewBox="0 0 24 24"><path fill="#10406f" d="M6.6 10.8a15 15 0 0 0 6.6 6.6l2.2-2.2c.3-.3.7-.4 1-.2 1.1.4 2.3.6 3.6.6.6 0 1 .4 1 1V20c0 .6-.4 1-1 1A17 17 0 0 1 3 4c0-.6.4-1 1-1h3.5c.6 0 1 .4 1 1 0 1.3.2 2.5.6 3.6.1.3 0 .7-.2 1z"/></svg>256 555 0148</div>
  </div>
</section>

<section class="card back">
  <div class="brand">
    <div class="brand-name">Penwick<span>Insurance</span></div>
    <div class="brand-tag">Specializing in Towing &amp; Transportation Insurance</div>
  </div>
  <div class="panel">
    <span class="tag about-tag">About Us</span>
    <p class="about">This agency was started with the idea of doing business in such a way that would look &amp; feel different than most agencies. Over time, we found a comfortable fit in the Towing, Transportation, &amp; Automotive industry which led us to committing our full attention to their insurance needs. We have partnered with over 20 companies that offer specialized insurance packages specifically for those types of businesses. We try hard to make each day purposeful and treat each customer as if they were our only one. I would have to say our motto is, "Be friendly to everyone, help all who ask for it, and work each day as if God Himself was handing you the paycheck</p>
    <span class="tag states-tag">Currently Representing The Following States</span>
    <div class="map" role="img" aria-label="Map of the eastern United States highlighting the represented states">
      <span class="state" style="left:26px;top:6px">Kentucky</span>
      <span class="state" style="left:128px;top:6px">North Carolina</span>
      <span class="state" style="left:18px;top:20px">South Carolina</span>
      <span class="state" style="left:26px;top:35px">Tennessee</span>
      <span class="state" style="left:20px;top:50px">Mississippi</span>
      <span class="state" style="left:146px;top:56px">Georgia</span>
      <span class="state" style="left:48px;top:66px">Alabama</span>
      <span class="state" style="left:150px;top:80px">Florida</span>
    </div>
  </div>
  <div class="footer">
    <div class="contact">
      <div><i class="icon"></i>penwickins-example.net</div>
      <div><i class="icon"></i>PenwickInfo@velmorlink.example</div>
    </div>
    <div class="phone"><svg viewBox="0 0 24 24"><path fill="#10406f" d="M6.6 10.8a15 15 0 0 0 6.6 6.6l2.2-2.2c.3-.3.7-.4 1-.2 1.1.4 2.3.6 3.6.6.6 0 1 .4 1 1V20c0 .6-.4 1-1 1A17 17 0 0 1 3 4c0-.6.4-1 1-1h3.5c.6 0 1 .4 1 1 0 1.3.2 2.5.6 3.6.1.3 0 .7-.2 1z"/></svg>256 555 0148</div>
  </div>
  <address class="address" style="font-style:normal">418 5th St NW,<br>Suite B Decatur,<br>AL 35602</address>
  <div class="stamp"></div>
  <div class="rule" style="top:260px"></div>
  <div class="rule" style="top:300px"></div>
  <div class="rule" style="top:339px"></div>
</section>

</body>
</html>
```